Label design - Superfood blend

We are a family owned nutrition company with big ambitions. Our goal is to develop a range of 100% natural supplements for women, inspired by nature & modern technology that helps them meet their nutritional needs while nourishing them from within. All our products are junk free because we believe that that’s how nature intended it. We also produce products through a sustainable process and only use biodegradable packaging for our products (See link - https://www.pouchwerk.example.uk/biodegradable-stand-pouch-250g-kraft)

Our brand style is modern and minimalist. This same style will be reflected in our social media, website and we want it to be represented through the label designs for our product packaging.

We want some creative designers to design a label that is true to our style (See attached packaging brief with designs we like) and displays our values of Premium, High Quality, Organic Real Food supplements focused on women. I have provided examples in the attached brief, but please only use as inspiration, I dont want any of them to be copied (sorry have had my fingers burnt already !)

Need extra days to review

Hello all, Please note this design is for a LABEL and not the whole package. We will have a 500gm biodegradable brown package, and we will have a label (which is what this project is about) that will be stuck on the front. The size of the label will be a rectangle (unless you come up with a new shape) in the size 20cm * 15cm. Please do not submit designs for the WHOLE from of the package, as we dont intend to have printed packages. Regards

Hello all, I have added a new logo version to the attachments, could you please also try that version. Could you also please look at the new sliders. We are only looking for a minimlaist theme. If you dont know what that means, please do feel free to ask, I would be happy to supply examples. Minimalist designs, means clean, modern, upmarket, elegant designs. It does not use too many colors and mostly sticks to a combination of black and white with colors used sparingly. See some below for your reference anyway. https://www.artbidhub.example.uk/design/48120573 https://www.artbidhub.example.uk/design/52961804 https://www.artbidhub.example.uk/design/47305916 https://www.artbidhub.example.uk/design/46719258 https://www.snapboardly.example.com/search/pins/?q=minimalist%20label%20design&rs=rs&eq=&etslf=2809&term_meta[]=minimalist%7Crecentsearch%7Cundefined&term_meta[]=label%7Crecentsearch%7Cundefined&term_meta[]=design%7Crecentsearch%7Cundefined Regards

Target Market(s)

The target market is women between the age 25 to 45, based in UK (mostly based in larger cities in UK). They are typically middle class or higher and would be in demanding jobs and social lives, that requires for them to meet their nutrition needs in convenient, easy to take forms. The women would also be socially conscious and sensitive to issues like women's rights, environmental issues, healthy food, organic food and sustainability etc. I have a much more detailed customer avatar if required

Font styles to use
Serif
Sans Serif
Decorative
Script

Colors
e8e8e8
474747
1b1b1b
add136

Requirements
Must have
• The label, should look minimalist and modern, throw in some out of the box creativity and we have a winner. Creativity will definitely be of importance. Our packaging is a biodegradable brown paper stand up pouch (Example link in product description). So to make it standout from other colorful packaging - being creative would definitely help.
• Please use the color schemes provided in the brief (See attachments). But if you want to experiment I would be open to it, as long as they are still minimalist and does not stray very far from the color given in the brief :)

```html
<!DOCTYPE html>
<html lang="en">
<head>
<meta charset="utf-8">
<title>Verdalia – Love Thy Core label concepts</title>
<link rel="stylesheet" href="https://fonts.googleapis.com/css2?family=Josefin+Sans:wght@400;600&family=Montserrat:wght@400;500&family=Oswald:wght@300&family=Dosis:wght@500&family=Caveat:wght@500&display=swap">
<style>
  :root{
    --canvas:#ececec;
    --ink:#111111;
    --label:#ffffff;
    --text:#474747;
    --band:#1b1f17;
    --green:#3f6b1f;
    --olive:#8a9a3a;
    --sage:#a7b596;
    --placeholder-green:#c9d5b8;
    --placeholder-sand:#e6dccf;
    --badge:#7a7a7a;
  }
  *{box-sizing:border-box;margin:0;padding:0}
  html,body{width:1200px;height:1200px;overflow:hidden;background:var(--canvas)}
  .board{width:1200px;height:1200px;position:relative}
  .board__heading{
    position:absolute;left:0;width:100%;text-align:center;
    font-family:"Josefin Sans",sans-serif;font-weight:400;font-size:46px;
    letter-spacing:9px;color:var(--ink)
  }
  .board__heading--top{top:18px}
  .board__heading--bottom{top:618px}
  .row{position:absolute;left:0;width:100%;display:flex;justify-content:space-around;padding:0 60px}
  .row--top{top:100px}
  .row--bottom{top:700px}

  .label{
    position:relative;width:250px;height:350px;background:var(--label);
    display:flex;flex-direction:column;align-items:center;
    font-family:"Montserrat",sans-serif;color:var(--text);
    box-shadow:0 2px 8px rgba(0,0,0,.08);overflow:hidden
  }
  .label__texture{position:absolute;inset:0}
  .label > *:not(.label__texture){position:relative}
  .texture--marble-leaf{background:linear-gradient(135deg,#f6f7f3 0%,#e6e9e0 45%,#f4f5f1 70%,#e3e7dc 100%)}
  .texture--geometric{background:linear-gradient(180deg,#faf9f1,#f3f2e6)}
  .texture--marble{background:linear-gradient(120deg,#f7f6f4 0%,#e9e6e2 40%,#f8f7f5 65%,#e7e4df 100%)}
  .texture--leaf-soft{background:linear-gradient(135deg,#ffffff 40%,#eef1e9 100%)}

  .brand{
    margin-top:34px;font-family:"Josefin Sans",sans-serif;font-size:21px;
    letter-spacing:5px;color:var(--ink);display:flex;align-items:center;gap:6px
  }
  .brand__dot{width:6px;height:6px;border-radius:50%;background:var(--green)}

  /* neutral placeholders for ornaments */
  .ornament{margin-top:10px;background:var(--placeholder-green)}
  .ornament--rosette{width:32px;height:32px}
  .ornament--crest{width:48px;height:26px;background:var(--placeholder-sand)}

  .title-frame{
    margin-top:10px;border:2px solid var(--green);
    padding:6px 12px;text-align:center;
    font-family:"Oswald",sans-serif;font-weight:300;font-size:32px;line-height:1.15;
    letter-spacing:4px;color:var(--ink)
  }
  .tagline{margin-top:10px;font-size:8px;letter-spacing:.8px;text-align:center;line-height:1.35;text-transform:uppercase}
  .band{
    margin-top:14px;background:var(--band);color:#fff;font-size:8px;letter-spacing:2.5px;
    padding:3px 12px;text-transform:uppercase
  }
  .footer{
    position:absolute !important;bottom:16px;left:16px;right:16px;
    display:flex;justify-content:space-between;align-items:center;font-size:8px
  }
  .badge{width:18px;height:18px;border-radius:50%;border:1.5px solid var(--badge)}
  .badge--leaf{border-color:var(--green)}

  /* centre concept */
  .tab{
    width:92px;height:132px;background:var(--sage);border-radius:0 0 46px 46px;
    display:flex;align-items:flex-end;justify-content:center;padding-bottom:12px
  }
  .tab__seal{
    width:72px;height:72px;border-radius:50%;border:1px solid rgba(255,255,255,.7);
    display:flex;align-items:center;justify-content:center;
    font-family:"Josefin Sans",sans-serif;font-size:8px;letter-spacing:1.5px;color:#2f3a24
  }
  .title-bracket{
    margin-top:26px;border-top:1.5px solid var(--ink);border-left:1.5px solid var(--ink);border-right:1.5px solid var(--ink);
    padding:4px 8px 0;font-family:"Dosis",sans-serif;font-weight:500;font-size:26px;color:var(--green);
    letter-spacing:.5px;white-space:nowrap
  }
  .supplement-note{margin-top:28px;font-size:8px;letter-spacing:1.5px;color:var(--olive);text-transform:uppercase}

  /* script concept */
  .title-script{
    margin-top:6px;font-family:"Caveat",cursive;font-weight:500;font-size:44px;line-height:.9;
    color:var(--green);text-align:center
  }
  .band-row{display:flex;align-items:center;gap:6px;margin-top:12px}
  .band-row .band{margin-top:0}
  .sprig{width:16px;height:26px;background:var(--placeholder-green)}
</style>
</head>
<body>
<main class="board">
  <h2 class="board__heading board__heading--top">WITH BACKGROUND</h2>
  <section class="row row--top">
    <article class="label label--classic">
      <div class="label__texture texture--marble-leaf" role="img" aria-label="Soft white marble texture with faint leaf silhouettes"></div>
      <div class="brand">VERDALIA<span class="brand__dot"></span></div>
      <div class="ornament ornament--rosette" role="img" aria-label="Small green flower ornament"></div>
      <h1 class="title-frame">LOVE<br>THY CORE</h1>
      <p class="tagline">Organic, plant-based<br>prebiotics and superfood blend</p>
      <p class="band">Food supplement</p>
      <div class="footer"><span>500gm</span><span class="badge badge--leaf"></span><span class="badge"></span></div>
    </article>

    <article class="label label--arch">
      <div class="label__texture texture--geometric" role="img" aria-label="Faint cream geometric line pattern"></div>
      <div class="tab"><div class="tab__seal">VERDALIA</div></div>
      <h1 class="title-bracket">LOVE THY CORE</h1>
      <p class="tagline">Organic, plant-based<br>prebiotics and superfood blend</p>
      <p class="supplement-note">Food supplement</p>
      <div class="footer"><span>500gm</span><span class="badge badge--leaf"></span><span class="badge"></span></div>
    </article>

    <article class="label label--script">
      <div class="label__texture texture--marble" role="img" aria-label="Light grey marble texture"></div>
      <div class="brand">VERDALIA<span class="brand__dot"></span></div>
      <div class="ornament ornament--crest" role="img" aria-label="Small rose-gold line ornament"></div>
      <h1 class="title-script">Love<br>Thy Core</h1>
      <p class="tagline">Organic, plant-based<br>prebiotics and superfood blend</p>
      <div class="band-row">
        <span class="sprig" role="img" aria-label="Green leaf sprig"></span>
        <p class="band">Food supplement</p>
        <span class="sprig" role="img" aria-label="Green leaf sprig"></span>
      </div>
      <div class="footer"><span>500gm</span><span class="badge badge--leaf"></span><span class="badge"></span></div>
    </article>
  </section>

  <h2 class="board__heading board__heading--bottom">WITHOUT BACKGROUND</h2>
  <section class="row row--bottom">
    <article class="label label--classic">
      <div class="label__texture texture--leaf-soft" role="img" aria-label="Faint leaf silhouettes on white"></div>
      <div class="brand">VERDALIA<span class="brand__dot"></span></div>
      <div class="ornament ornament--rosette" role="img" aria-label="Small green flower ornament"></div>
      <h1 class="title-frame">LOVE<br>THY CORE</h1>
      <p class="tagline">Organic, plant-based<br>prebiotics and superfood blend</p>
      <p class="band">Food supplement</p>
      <div class="footer"><span>500gm</span><span class="badge badge--leaf"></span><span class="badge"></span></div>
    </article>

    <article class="label label--arch">
      <div class="tab"><div class="tab__seal">VERDALIA</div></div>
      <h1 class="title-bracket">LOVE THY CORE</h1>
      <p class="tagline">Organic, plant-based<br>prebiotics and superfood blend</p>
      <p class="supplement-note">Food supplement</p>
      <div class="footer"><span>500gm</span><span class="badge badge--leaf"></span><span class="badge"></span></div>
    </article>

    <article class="label label--script">
      <div class="brand">VERDALIA<span class="brand__dot"></span></div>
      <div class="ornament ornament--crest" role="img" aria-label="Small rose-gold line ornament"></div>
      <h1 class="title-script">Love<br>Thy Core</h1>
      <p class="tagline">Organic, plant-based<br>prebiotics and superfood blend</p>
      <div class="band-row">
        <span class="sprig" role="img" aria-label="Green leaf sprig"></span>
        <p class="band">Food supplement</p>
        <span class="sprig" role="img" aria-label="Green leaf sprig"></span>
      </div>
      <div class="footer"><span>500gm</span><span class="badge badge--leaf"></span><span class="badge"></span></div>
    </article>
  </section>
</main>
</body>
</html>
```